Business Card Revision

Need to redesign my business cards for a new professional look. We are a courier company. You can go to www.qvrunners.com to see what we do. The trucks have an old company name (Sprout) on them but that is the company we are just now
changing the name.

Target Market(s)

Potential clients. We service the automotive, plumbing, printing, air freight industries as well as many others.

Industry/Entity Type

Business

Contact Information for Business Card

QVmotion
20864 Lark Fenmore Parkway
Cincinnati, Oh 45873

Thomas R. Wendall
President

tom@qvrunners.com

Main: (513) 555-0147

```html
<!DOCTYPE html>
<html lang="en">
<head>
<meta charset="utf-8">
<title>QV Runners Business Card</title>
<link href="https://fonts.googleapis.com/css2?family=Open+Sans:wght@400;600;700;800&display=swap" rel="stylesheet">
<style>
  :root {
    --backdrop: #d9d9d9;
    --brand-blue: #0e72bd;
    --brand-green: #3cb44b;
    --ink-black: #000000;
    --paper-white: #ffffff;
  }
  * { margin: 0; padding: 0; box-sizing: border-box; }
  html, body {
    width: 1200px;
    height: 900px;
    overflow: hidden;
    background: var(--backdrop);
    font-family: "Open Sans", Arial, sans-serif;
  }
  .sheet {
    position: relative;
    width: 1200px;
    height: 900px;
  }
  .card {
    position: absolute;
    left: 240px;
    width: 720px;
    height: 411px;
    overflow: hidden;
    box-shadow: 0 4px 14px rgba(0,0,0,0.18);
  }
  .card-front {
    top: 26px;
    background: var(--brand-blue);
    display: flex;
    align-items: center;
    justify-content: center;
  }
  .card-back {
    top: 463px;
    background: var(--brand-blue);
  }
  .wordmark {
    color: var(--paper-white);
    font-weight: 800;
    font-size: 64px;
    letter-spacing: 3px;
    line-height: 1;
    display: flex;
    align-items: center;
    gap: 18px;
  }
  .wordmark-dot {
    width: 22px;
    height: 22px;
    background: currentColor;
  }
  .card-back .swoosh {
    position: absolute;
    inset: 0;
    width: 100%;
    height: 100%;
  }
  .card-back .wordmark {
    position: absolute;
    left: 70px;
    top: 150px;
    font-size: 46px;
    letter-spacing: 2px;
    color: var(--brand-green);
  }
  .contact {
    position: absolute;
    right: 46px;
    top: 118px;
    text-align: right;
    color: var(--paper-white);
  }
  .contact-name {
    font-weight: 700;
    font-size: 24px;
    line-height: 1.1;
  }
  .contact-title {
    font-size: 18px;
    margin-bottom: 14px;
  }
  .contact-address {
    font-size: 18px;
    line-height: 1.3;
    margin-bottom: 16px;
  }
  .contact-lines {
    list-style: none;
    font-size: 18px;
    line-height: 1.5;
  }
  .contact-lines li {
    display: flex;
    align-items: center;
    justify-content: flex-end;
    gap: 12px;
  }
  .contact-icon {
    width: 15px;
    height: 15px;
    flex: none;
  }
</style>
</head>
<body>
<main class="sheet">

  <section class="card card-front">
    <div class="wordmark"><span class="wordmark-dot"></span>QV RUNNERS</div>
  </section>

  <section class="card card-back">
    <svg class="swoosh" viewBox="0 0 720 411" preserveAspectRatio="none" aria-hidden="true">
      <path d="M0,0 H440 C520,130 470,320 320,411 H0 Z" fill="var(--brand-green)"/>
      <path d="M0,0 H420 C495,130 448,315 290,411 H0 Z" fill="var(--ink-black)"/>
      <path d="M436,0 C512,128 464,316 318,411" fill="none" stroke="var(--ink-black)" stroke-width="3"/>
    </svg>

    <div class="wordmark">QV RUNNERS</div>

    <div class="contact">
      <p class="contact-name">Thomas R. Wendall</p>
      <p class="contact-title">President</p>
      <p class="contact-address">20864 Lark Fenmore Parkway<br>Cincinnati, Oh 45873</p>
      <ul class="contact-lines">
        <li>(513) 555-0147
          <svg class="contact-icon" viewBox="0 0 16 16" aria-hidden="true"><path fill="#fff" d="M3.5 1.5l2.5 0 1 3.5-1.6 1.2a8 8 0 0 0 4.4 4.4L11 9l3.5 1v2.5c0 .8-.7 1.5-1.5 1.5A11 11 0 0 1 2 3c0-.8.7-1.5 1.5-1.5z"/></svg>
        </li>
        <li>tom@qvrunners.com
          <svg class="contact-icon" viewBox="0 0 16 16" aria-hidden="true"><rect x="1" y="3" width="14" height="10" rx="1" fill="#fff"/><path d="M1.5 3.8L8 9l6.5-5.2" fill="none" stroke="var(--brand-blue)" stroke-width="1.3"/></svg>
        </li>
        <li>www.qvrunners.com
          <svg class="contact-icon" viewBox="0 0 16 16" aria-hidden="true"><circle cx="8" cy="8" r="7" fill="#fff"/><path d="M1 8h14M8 1c-3 3-3 11 0 14M8 1c3 3 3 11 0 14" fill="none" stroke="var(--brand-blue)" stroke-width="1.1"/></svg>
        </li>
      </ul>
    </div>
  </section>

</main>
</body>
</html>
```